Nera Bloom Fitness Coaching Project

I am a personal trainer based in London. My services include one-on-one PT sessions, bootcamps.
I would like the design to be minimalistic. With light colours: white, pink, purple.
I specialise in weight loss, flexibility, mobility.

Orla Pemvick
Personal Trainer
Email: orla.pemvick@tovamail.com
tel: 07400918243
pictafeed: Nera Bloom

Target Market(s)

adults, mostly females (age 18-50).

Industry/Entity Type

Fitness

Contact Information for Business Card

Orla Pemvick
Personal Trainer
tel: 07400918243
pictafeed: Nera Bloom

Font styles to use
Serif

Colors
eea4c8
fbd4d5
fdf9cf
cfeae6
cee9f5

Requirements
Nice to have
• minimalistic style
• easy to read and remember

```html
<!DOCTYPE html>
<html lang="en">
<head>
<meta charset="utf-8">
<title>Orla Pemvick – Business Card</title>
<link href="https://fonts.googleapis.com/css2?family=Crimson+Pro:wght@400;500&display=swap" rel="stylesheet">
<style>
  :root {
    --canvas-bg: #ecebea;
    --card-top: #ffffff;
    --card-bottom: #f1efee;
    --brand-pink: #e7a0c6;
    --band-pink: #dd9cc4;
    --ink: #1f1f1f;
    --photo-pink: #e0307c;
    --photo-teal: #3fb4c0;
    --portrait-dark: #3a2a22;
    --portrait-warm: #a8745a;
  }
  * { box-sizing: border-box; margin: 0; padding: 0; }
  html, body {
    width: 1200px; height: 1000px; overflow: hidden;
    background: var(--canvas-bg);
    font-family: "Crimson Pro", "Times New Roman", serif;
  }
  .canvas { position: relative; width: 1200px; height: 1000px; }

  .card {
    position: absolute;
    width: 640px; height: 362px;
    background: linear-gradient(180deg, var(--card-top) 0%, var(--card-top) 55%, var(--card-bottom) 100%);
    box-shadow: 0 6px 18px rgba(0,0,0,0.12);
    overflow: hidden;
  }
  .card__band {
    position: absolute; left: 0; right: 0; bottom: 0;
    height: 22px; background: var(--band-pink);
  }

  /* Front */
  .card--front { left: 280px; top: 90px; }
  .portrait {
    position: absolute; left: 252px; top: 32px;
    width: 136px; height: 136px; border-radius: 50%;
    background: radial-gradient(circle at 50% 45%, var(--portrait-warm) 0%, var(--portrait-dark) 75%);
  }
  .identity {
    position: absolute; right: 342px; top: 208px;
    text-align: right;
  }
  .identity__name {
    color: var(--brand-pink);
    font-size: 36px; font-weight: 400; line-height: 1;
    letter-spacing: 0.3px;
  }
  .identity__role {
    margin-top: 12px;
    font-size: 18px; color: var(--ink);
    padding-right: 34px;
  }
  .divider {
    position: absolute; left: 321px; top: 198px;
    width: 2px; height: 94px; background: var(--brand-pink);
  }
  .contacts {
    position: absolute; left: 342px; top: 213px;
    list-style: none;
  }
  .contacts__item {
    display: flex; align-items: center; gap: 10px;
    font-size: 19px; color: var(--ink); letter-spacing: 1px;
    height: 26px;
  }
  .contacts__item + .contacts__item { margin-top: 18px; letter-spacing: 0.5px; }
  .contacts__icon { width: 17px; height: 17px; flex: none; }

  /* Back */
  .card--back { left: 280px; top: 540px; }
  .action-photo {
    position: absolute; left: 0; top: 0;
    width: 640px; height: 254px;
    background: linear-gradient(180deg, var(--photo-pink) 0%, var(--photo-pink) 30%, var(--photo-teal) 48%, var(--photo-teal) 100%);
  }
  .social {
    position: absolute; left: 0; right: 0; top: 282px;
    display: flex; justify-content: center; align-items: center; gap: 12px;
    font-size: 21px; color: var(--ink); letter-spacing: 0.4px;
  }
  .social__mark {
    width: 26px; height: 26px; border-radius: 4px;
    background: var(--brand-pink);
  }
</style>
</head>
<body>
<main class="canvas">

  <section class="card card--front">
    <div class="portrait" role="img" aria-label="Round portrait photo of the trainer"></div>
    <div class="identity">
      <h1 class="identity__name">Orla Pemvick</h1>
      <p class="identity__role">Personal Trainer</p>
    </div>
    <div class="divider"></div>
    <ul class="contacts">
      <li class="contacts__item">
        <svg class="contacts__icon" viewBox="0 0 24 24" aria-hidden="true">
          <path d="M6.6 10.8a15.1 15.1 0 0 0 6.6 6.6l2.2-2.2c.3-.3.7-.4 1-.2 1.1.4 2.3.6 3.6.6.6 0 1 .4 1 1V20c0 .6-.4 1-1 1A17 17 0 0 1 3 4c0-.6.4-1 1-1h3.5c.6 0 1 .4 1 1 0 1.3.2 2.5.6 3.6.1.3 0 .7-.2 1L6.6 10.8z" fill="none" stroke="#e7a0c6" stroke-width="2"/>
        </svg>
        <span>07400918243</span>
      </li>
      <li class="contacts__item">
        <svg class="contacts__icon" viewBox="0 0 24 24" aria-hidden="true">
          <rect x="2" y="5" width="20" height="14" fill="none" stroke="#e7a0c6" stroke-width="2"/>
          <path d="M2 5l10 8 10-8" fill="none" stroke="#e7a0c6" stroke-width="2"/>
        </svg>
        <span>orla.pemvick@tovamail.com</span>
      </li>
    </ul>
    <div class="card__band"></div>
  </section>

  <section class="card card--back">
    <div class="action-photo" role="img" aria-label="Photo of the trainer doing a high kick in front of a pink and teal mural"></div>
    <p class="social">
      <span class="social__mark" aria-hidden="true"></span>
      <span>pictafeed/Nera Bloom</span>
    </p>
    <div class="card__band"></div>
  </section>

</main>
</body>
</html>
```